Business card and stationary for consulting business

We need business cards and matching stationary for professional consulting business for employment and human resources issues.
One of the CraftHive designers designed the logo with our company name.  Use the colors in the logo and may use light yellow as an accent color.
Add
Mara T. Vollen, J.D., LL.M.
485 E. Callister Lane
Winter Park, Florida  32789
407-555-0183
maravollenjd@quillpost.example

Industry/Entity Type
Business

```html
<!DOCTYPE html>
<html lang="en">
<head>
<meta charset="utf-8">
<title>Callistra – Business Card</title>
<link href="https://fonts.googleapis.com/css2?family=Titillium+Web:wght@300;400;600&display=swap" rel="stylesheet">
<style>
  :root{
    --page:#eef1f3;
    --card-white:#ffffff;
    --blue-light:#6fd0e8;
    --blue-mid:#37b2e0;
    --blue-deep:#1f96cf;
    --brand:#1d6f9f;
    --text-grey:#6b7a86;
    --on-blue:#ffffff;
  }
  *{box-sizing:border-box;margin:0;padding:0}
  html,body{width:1200px;height:870px;overflow:hidden}
  body{
    background:var(--page);
    font-family:"Titillium Web",Arial,sans-serif;
    display:flex;align-items:center;justify-content:center;gap:60px;
  }
  .card{
    position:relative;width:525px;height:300px;overflow:hidden;
    box-shadow:0 8px 24px rgba(30,60,80,.18);
  }
  /* Back: company side */
  .card-back{background:var(--card-white)}
  .card-back .edge-curve{position:absolute;right:0;top:0;height:100%;width:120px}
  .brand-lockup{
    position:absolute;left:48px;top:50%;transform:translateY(-50%);
    display:flex;flex-direction:column;gap:10px;
  }
  .brand-name{
    display:flex;align-items:center;gap:10px;
    font-size:38px;font-weight:400;color:var(--brand);letter-spacing:.5px;line-height:1;
  }
  .brand-mark{width:12px;height:12px;border-radius:50%;background:var(--brand)}
  .tagline{
    list-style:none;display:flex;gap:14px;
    font-size:12px;line-height:1.3;color:var(--text-grey);font-weight:400;
    text-transform:uppercase;letter-spacing:1px;
  }
  /* Front: contact side */
  .card-front{
    background:radial-gradient(ellipse at 40% 70%,var(--blue-light) 0%,var(--blue-mid) 50%,var(--blue-deep) 100%);
    color:var(--on-blue);
  }
  .person{position:absolute;left:36px;top:34px}
  .person-name{font-size:24px;font-weight:600;letter-spacing:1.5px;line-height:1.1}
  .person-role{font-size:15px;font-weight:300;letter-spacing:.5px;margin-top:2px}
  .contact-list{
    position:absolute;right:32px;bottom:30px;list-style:none;text-align:right;
    font-size:14px;font-weight:400;line-height:1.35;
  }
  .contact-list li{display:flex;align-items:center;justify-content:flex-end;gap:10px;margin-top:4px}
  .contact-list .address{margin-bottom:10px;line-height:1.3}
  .contact-icon{width:14px;height:14px;flex:none}
</style>
</head>
<body>

<section class="card card-back" aria-label="Card back with company name">
  <div class="brand-lockup">
    <div class="brand-name"><span class="brand-mark"></span><span>Callistra</span></div>
    <ul class="tagline">
      <li>People</li>
      <li>Policy</li>
      <li>Practice</li>
    </ul>
  </div>
  <svg class="edge-curve" viewBox="0 0 120 300" preserveAspectRatio="none" aria-hidden="true">
    <path d="M120 0 L70 0 Q20 150 70 300 L120 300 Z" fill="#37b2e0"/>
    <path d="M70 0 Q20 150 70 300 L60 300 Q8 150 60 0 Z" fill="#1f96cf"/>
  </svg>
</section>

<section class="card card-front" aria-label="Card front with contact details">
  <div class="person">
    <h1 class="person-name">MARA T. VOLLEN</h1>
    <p class="person-role">Managing Director</p>
  </div>
  <ul class="contact-list">
    <li class="address"><span>485 E. Callister Lane<br>Winter Park, Florida 32789</span></li>
    <li><span>407 555 0183</span>
      <svg class="contact-icon" viewBox="0 0 16 16" aria-hidden="true"><path d="M4 1l3 3-2 2q1.5 3 5 5l2-2 3 3-2 3Q5 14 1 3z" fill="#fff"/></svg></li>
    <li><span>407 555 0184</span>
      <svg class="contact-icon" viewBox="0 0 16 16" aria-hidden="true"><rect x="4" y="1" width="8" height="14" rx="1.5" fill="none" stroke="#fff" stroke-width="1.6"/><circle cx="8" cy="12.5" r="1" fill="#fff"/></svg></li>
    <li><span>407 555 0185</span>
      <svg class="contact-icon" viewBox="0 0 16 16" aria-hidden="true"><rect x="2" y="6" width="12" height="8" fill="#fff"/><rect x="4" y="1" width="8" height="5" fill="none" stroke="#fff" stroke-width="1.5"/></svg></li>
    <li><span>maravollenjd@quillpost.example</span>
      <svg class="contact-icon" viewBox="0 0 16 16" aria-hidden="true"><rect x="1" y="3" width="14" height="10" fill="#fff"/><path d="M1 3l7 6 7-6" fill="none" stroke="#37b2e0" stroke-width="1.4"/></svg></li>
    <li><span>www.quillpost.example</span>
      <svg class="contact-icon" viewBox="0 0 16 16" aria-hidden="true"><g fill="none" stroke="#fff" stroke-width="1.3"><circle cx="8" cy="8" r="6.5"/><ellipse cx="8" cy="8" rx="3" ry="6.5"/><path d="M1.5 8h13"/></g></svg></li>
  </ul>
</section>

</body>
</html>
```